Local Flower Farm Needs Business Card Design

I need business cards designed for a flower farm based in Eudora, Kansas.
Business Info:
We are a local cut flower farm located in Eudora, Kansas, founded by Darla Hoffstrom. What started as a passion for agriculture and search for more joy in daily life has blossomed into a small business dedicated to providing the community with beautiful, fresh, and sustainable flowers. We specialize in local, seasonal blooms, ensuring that every petal reflects the care and dedication we pour into our craft. Our mission is to deliver the highest quality flowers directly to our customers through local farmers markets and to florists who share our commitment to sustainability. Join us in celebrating the beauty of nature, one bloom at a time!
Contact Details:
Darla Hoffstrom
Owner
Phone 913-555-0147
Facebook: Lorabelle Quinn Blossoms
Instagram: @LorabelleQuinnBlossoms
Website: LorabelleQuinnBlossoms.example
Target Market(s)
Wholesale to Florists and Direct to Consumer via Farmers Market
Industry/Entity Type
Florist, Farm
Contact Information for Business Card
Name, Contact Info, Logo
Look and feel

```html
<!DOCTYPE html>
<html lang="en">
<head>
<meta charset="utf-8">
<title>Lorabelle Quinn Blossoms — Business Card</title>
<link rel="stylesheet" href="https://fonts.googleapis.com/css2?family=Montserrat:wght@500;600;700&display=swap">
<style>
  :root {
    --backdrop: #e2e2e2;
    --evergreen: #06262d;
    --paper: #fbfbfb;
    --ink: #06262d;
    --slate: #3d3f42;
    --muted: #6f6f6f;
    --on-dark: #ffffff;
  }
  * { box-sizing: border-box; margin: 0; padding: 0; }
  html, body { width: 1200px; height: 1200px; overflow: hidden; }
  body {
    background: var(--backdrop);
    font-family: "Montserrat", Arial, sans-serif;
    position: relative;
  }
  .card {
    position: absolute;
    left: 179px;
    width: 861px;
    height: 495px;
    box-shadow: 0 10px 22px rgba(0,0,0,0.18);
  }
  .card--front { top: 84px; background: var(--evergreen); }
  .card--back { top: 621px; background: var(--paper); }

  .brand {
    position: absolute;
    border-radius: 50%;
    display: flex;
    flex-direction: column;
    align-items: center;
    justify-content: center;
    text-align: center;
    font-weight: 600;
    text-transform: uppercase;
    line-height: 1.3;
  }
  .card--front .brand {
    left: 289px; top: 124px; width: 230px; height: 230px;
    border: 1.5px solid var(--on-dark);
    color: var(--on-dark);
    font-size: 20px; letter-spacing: 3px;
  }
  .card--back .brand {
    left: 337px; top: 45px; width: 187px; height: 187px;
    border: 1.5px solid var(--ink);
    color: var(--ink);
    font-size: 16px; letter-spacing: 2.4px;
  }

  .holder {
    position: absolute;
    top: 254px;
    left: 0; right: 0;
    text-align: center;
  }
  .holder__name {
    font-size: 34px;
    font-weight: 700;
    color: var(--ink);
    letter-spacing: 0.8px;
    margin-left: 34px;
    line-height: 1.2;
  }
  .holder__role {
    font-size: 24px;
    font-weight: 500;
    color: var(--muted);
    letter-spacing: 1.2px;
    line-height: 1.2;
    margin-top: 0;
  }

  .contact { position: absolute; top: 360px; left: 0; right: 0; height: 70px; }
  .contact__divider {
    position: absolute; left: 447px; top: 0; width: 1px; height: 64px;
    background: var(--slate);
  }
  .contact__row {
    position: absolute; display: flex; align-items: center; gap: 10px;
    font-size: 18px; font-weight: 600; color: var(--slate); letter-spacing: 2px;
    white-space: nowrap; height: 22px;
  }
  .contact__row--left { right: 425px; }
  .contact__row--right { left: 459px; }
  .contact__row--top { top: 2px; }
  .contact__row--bottom { top: 37px; }
  .icon {
    width: 20px; height: 20px; background: var(--ink); flex: none;
    display: flex; align-items: center; justify-content: center;
  }
</style>
</head>
<body>
  <section class="card card--front">
    <div class="brand">
      <span>Lorabelle</span>
      <span>Quinn</span>
      <span>Blossoms</span>
    </div>
  </section>

  <section class="card card--back">
    <div class="brand">
      <span>Lorabelle</span>
      <span>Quinn</span>
      <span>Blossoms</span>
    </div>

    <div class="holder">
      <p class="holder__name">Darla Hoffstrom</p>
      <p class="holder__role">Owner</p>
    </div>

    <div class="contact">
      <div class="contact__row contact__row--left contact__row--top">
        <span>913-555-0147</span>
        <span class="icon">
          <svg width="14" height="14" viewBox="0 0 24 24" aria-hidden="true">
            <path fill="#fff" d="M6.6 10.8a15.1 15.1 0 0 0 6.6 6.6l2.2-2.2a1 1 0 0 1 1-.25 11.4 11.4 0 0 0 3.6.57 1 1 0 0 1 1 1V20a1 1 0 0 1-1 1A17 17 0 0 1 3 4a1 1 0 0 1 1-1h3.5a1 1 0 0 1 1 1c0 1.25.2 2.45.57 3.57a1 1 0 0 1-.25 1z"/>
          </svg>
        </span>
      </div>
      <div class="contact__row contact__row--left contact__row--bottom">
        <span>LorabelleQuinnBlossoms.example</span>
        <span class="icon">
          <svg width="14" height="14" viewBox="0 0 24 24" aria-hidden="true">
            <circle cx="12" cy="12" r="9" fill="none" stroke="#fff" stroke-width="2"/>
            <ellipse cx="12" cy="12" rx="4" ry="9" fill="none" stroke="#fff" stroke-width="1.6"/>
            <line x1="3" y1="12" x2="21" y2="12" stroke="#fff" stroke-width="1.6"/>
          </svg>
        </span>
      </div>

      <span class="contact__divider"></span>

      <div class="contact__row contact__row--right contact__row--top">
        <span class="icon">
          <svg width="14" height="14" viewBox="0 0 24 24" aria-hidden="true">
            <path fill="#fff" d="M4 4h16a1 1 0 0 1 1 1v11a1 1 0 0 1-1 1H10l-5 4v-4H4a1 1 0 0 1-1-1V5a1 1 0 0 1 1-1z"/>
          </svg>
        </span>
        <span>@LorabelleQuinnBlossoms</span>
      </div>
      <div class="contact__row contact__row--right contact__row--bottom">
        <span class="icon">
          <svg width="14" height="14" viewBox="0 0 24 24" aria-hidden="true">
            <path fill="#fff" d="M12 21s-8-5.2-8-11a4.5 4.5 0 0 1 8-2.8A4.5 4.5 0 0 1 20 10c0 5.8-8 11-8 11z"/>
          </svg>
        </span>
        <span>@LorabelleQuinnBlossoms</span>
      </div>
    </div>
  </section>
</body>
</html>
```